Business card design needed

I would like a one sided black business card with the information provided above. Refer to my website www.lobcrafttennis.com.au for an example of colors I have used for my site, would like to keep this consistent for my business cards also, I will upload my logo below.

I am a new small business that provides tennis customers with racquet re stringing, tennis strings and accessories.

Industry/Entity Type

Small Business

Contact Information for Business Card

Lob Craft Tennis

Dennis Morrow
Managing Director

lobcrafttennis@mailbay.com
www.lobcrafttennis.com.au
0412 695 203

Racquet Restringing/Tennis Strings/Accessories

Requirements
Must have
• Must have my logo and card must be black

```html
<!DOCTYPE html>
<html lang="en">
<head>
<meta charset="utf-8">
<title>Lob Craft Tennis Business Card</title>
<link rel="stylesheet" href="https://fonts.googleapis.com/css2?family=Exo+2:wght@400;600&family=Oswald:wght@500&display=swap">
<style>
  :root {
    --backdrop: #d9d9d9;
    --card-black: #0b0b0b;
    --lime: #c6df2a;
    --white: #ffffff;
    --muted-white: #e8e8e8;
    --photo-dark: #151515;
    --photo-ball: #8fa51c;
  }
  * { margin: 0; padding: 0; box-sizing: border-box; }
  html, body {
    width: 1200px;
    height: 861px;
    overflow: hidden;
    background: var(--backdrop);
  }
  .stage {
    width: 1200px;
    height: 861px;
    display: flex;
    align-items: center;
    justify-content: center;
  }
  .business-card {
    position: relative;
    width: 900px;
    height: 514px;
    background: var(--card-black);
    overflow: hidden;
    font-family: "Exo 2", sans-serif;
    color: var(--white);
  }
  .product-photo {
    position: absolute;
    top: 0;
    right: 0;
    width: 480px;
    height: 100%;
    background:
      radial-gradient(circle at 62% 32%, var(--photo-ball) 0%, #5c6c14 22%, rgba(20,20,20,0) 42%),
      radial-gradient(circle at 38% 78%, rgba(143,165,28,0.35) 0%, rgba(20,20,20,0) 30%),
      linear-gradient(90deg, var(--card-black) 0%, var(--photo-dark) 30%, #222 100%);
  }
  .brand {
    position: absolute;
    top: 58px;
    left: 48px;
    display: flex;
    align-items: center;
    gap: 14px;
  }
  .brand-dot {
    width: 34px;
    height: 34px;
    border-radius: 50%;
    background: var(--lime);
  }
  .brand-name {
    font-weight: 600;
    font-size: 36px;
    letter-spacing: 1px;
    color: var(--lime);
    text-transform: uppercase;
  }
  .person {
    position: absolute;
    top: 150px;
    left: 48px;
  }
  .person-name {
    font-weight: 600;
    font-size: 46px;
    color: var(--lime);
    line-height: 1.1;
  }
  .person-title {
    font-weight: 400;
    font-size: 27px;
    color: var(--muted-white);
    margin-top: 4px;
  }
  .contact-list {
    position: absolute;
    top: 285px;
    left: 48px;
    list-style: none;
  }
  .contact-list li {
    font-size: 25px;
    line-height: 48px;
    color: var(--white);
  }
  .contact-label {
    display: inline-block;
    width: 30px;
    font-weight: 600;
    color: var(--lime);
  }
  .services {
    position: absolute;
    right: 44px;
    bottom: 62px;
    text-align: right;
    font-family: "Oswald", sans-serif;
    font-weight: 500;
    font-size: 28px;
    line-height: 1.25;
    letter-spacing: 1px;
    text-transform: uppercase;
    color: var(--white);
  }
  .services .slash { color: var(--lime); }
</style>
</head>
<body>
  <main class="stage">
    <section class="business-card">
      <div class="product-photo" role="img" aria-label="Close-up photo of a yellow tennis ball resting on racquet strings"></div>

      <div class="brand">
        <span class="brand-dot"></span>
        <span class="brand-name">Lob Craft Tennis</span>
      </div>

      <div class="person">
        <h1 class="person-name">Dennis Morrow</h1>
        <p class="person-title">Managing Director</p>
      </div>

      <ul class="contact-list">
        <li><span class="contact-label">P</span>0412 695 203</li>
        <li><span class="contact-label">E</span>lobcrafttennis@mailbay.com</li>
        <li><span class="contact-label">W</span>www.lobcrafttennis.com.au</li>
      </ul>

      <p class="services">
        Racquet Restringing<span class="slash">/</span><br>
        Tennis Strings<span class="slash">/</span>Accessories
      </p>
    </section>
  </main>
</body>
</html>
```